Lotuvan Cafe Menu rev.01

Design an elegant menu for Khmer restaurant in Melbourne.

-Size and format can be proposed (not bigger than A3)
-Food and beverages split (separate sides of the menu)
-Sample excel file - Food attached
-Sample Menu Pdf attached (just to get an idea)
-Details shall be reviewed and considered
-Prices in AUD
-Easy to print and clean (format need to to printable)
-Provision for future updates.

If you have any further question please let us know.
Regards,

Dexter

Target Market(s)

Customers win the restaurant

Industry/Entity Type

Hospitality - Restaurant

Colors

Designer to choose colors to be used in the design.

Requirements
Must have
• Authentic touch - clear structure
Nice to have
• Welcome about the restaurant. Complete information - see sample menu

```html
<!DOCTYPE html>
<html lang="en">
<head>
<meta charset="utf-8">
<title>Lotuvan Cafe &amp; Restaurant — Menu</title>
<link rel="stylesheet" href="https://fonts.googleapis.com/css2?family=Poppins:wght@400;500&family=Marcellus&family=Playfair+Display:wght@400&family=Cutive+Mono&display=swap">
<style>
  :root {
    --stage: #e6e4df;
    --paper: #f7f7f5;
    --gold: #a4975a;
    --ink: #1e1e1e;
    --muted: #3c3c3c;
    --rule: #2a2a2a;
    --veg: #7cb342;
    --vegan: #2e7d32;
    --gf: #f29a2e;
    --chili: #d3302a;
  }
  * { box-sizing: border-box; margin: 0; padding: 0; }
  html, body { width: 1200px; height: 1200px; overflow: hidden; background: var(--stage); }
  body { position: relative; font-family: "Poppins", sans-serif; color: var(--ink); }

  .sheet {
    position: absolute; left: 0; top: 0;
    width: 1200px; height: 850px;
    background: var(--paper);
    overflow: hidden;
    transform-origin: 0 0;
    box-shadow: 0 6px 18px rgba(0,0,0,.18);
  }
  .sheet-back  { transform: translate(360px, 603px) scale(.69); }
  .sheet-front { transform: translate(12px, 10px) scale(.69); }
  .abs { position: absolute; }

  .brand-name { font-family: "Marcellus", serif; color: var(--gold); text-align: center; letter-spacing: 1px; }

  .menu-title {
    font-family: "Playfair Display", serif; font-weight: 400;
    letter-spacing: 22px; padding-left: 22px; text-align: center;
  }
  .title-rule { height: 1px; background: var(--rule); }

  .section-head {
    border-top: 1px solid var(--rule); border-right: 1px solid var(--rule); border-bottom: 1px solid var(--rule);
    font-family: "Marcellus", serif; font-weight: 400; color: var(--gold);
    font-size: 22px; letter-spacing: 1.5px; height: 46px; padding-top: 8px; width: 332px;
  }
  .section-head.boxed { border-left: 1px solid var(--rule); }

  .dish-list { display: flex; flex-direction: column; gap: 10px; }
  .dish-head { display: grid; grid-template-columns: 1fr 44px; column-gap: 8px; align-items: start; }
  .dish-name { font-size: 13.5px; font-weight: 500; letter-spacing: .3px; line-height: 19px; }
  .dish-price { font-size: 12.5px; color: var(--gold); line-height: 19px; }
  .dish-price small { display: block; font-size: 6.5px; line-height: 8px; white-space: nowrap; }
  .dish-desc { font-size: 9.8px; line-height: 13px; color: var(--muted); margin-top: 4px; width: 240px; }

  .plate { border-radius: 50%; box-shadow: 0 4px 8px rgba(0,0,0,.18); border: 4px solid #fff; }

  .about { display: flex; flex-direction: column; gap: 14px; font-size: 10px; line-height: 14px; color: var(--muted); width: 252px; }

  .legend { font-family: "Cutive Mono", monospace; color: var(--muted); display: flex; flex-wrap: wrap; align-items: center; }
  .legend span { display: inline-flex; align-items: center; gap: 4px; }
  .dot { border-radius: 50%; display: inline-block; }

  .side-list { display: flex; flex-direction: column; gap: 9px; width: 300px; }
  .side-list .dish-head { grid-template-columns: 1fr 50px; }

  .notes { list-style: none; font-size: 10px; line-height: 13px; color: var(--muted); display: flex; flex-direction: column; gap: 3px; }
  .notes li { padding-left: 12px; position: relative; }
  .notes li::before { content: ""; position: absolute; left: 0; top: 4px; width: 5px; height: 5px; border-radius: 50%; background: var(--ink); }
</style>
</head>
<body>

<!-- Back side: curries, desserts, salads, side dishes -->
<section class="sheet sheet-back">
  <div class="abs dish-list" style="left:60px; top:36px; width:320px;">
    <div class="dish">
      <div class="dish-head"><span class="dish-name">Fish Amok</span><span class="dish-price"></span></div>
      <p class="dish-desc">Traditional Cambodian steamed in banana leaf, Markel fish, curry paste, coconut, Chinese Broccoli served with Jasmine rice.</p>
    </div>
    <div class="dish">
      <div class="dish-head"><span class="dish-name">Red Curry</span><span class="dish-price">$17.00</span></div>
      <p class="dish-desc">Red Curry with chicken &amp; vegetable.</p>
    </div>
    <div class="dish">
      <div class="dish-head"><span class="dish-name">Green Curry</span><span class="dish-price">$17.00<small>Fish (+$3.00)</small></span></div>
      <p class="dish-desc">Green Curry with Beef or Fish (Markel filet), with pineapple, eggplant &amp; bamboo).</p>
    </div>
    <div class="dish">
      <div class="dish-head"><span class="dish-name">Kampot Pepper with Seafood</span><span class="dish-price">$25.00</span></div>
      <p class="dish-desc">Kampot Pepper with Seafood, onion, carrot &amp; dust of Spring onion.</p>
    </div>
    <div class="dish">
      <div class="dish-head"><span class="dish-name">Char Kreung Chicken or Fish</span><span class="dish-price">$22.00<small>Fish (+$3.00)</small></span></div>
      <p class="dish-desc">Stirred-fried of commination chicken or fish, mix vegetable, green beans, sweet chilli .</p>
    </div>
    <div class="dish">
      <div class="dish-head"><span class="dish-name">Beef Loc Lac</span><span class="dish-price">$24.00</span></div>
      <p class="dish-desc">Cambodian marinated beef chunks and vegetable served with crispy sweet potato strips.</p>
    </div>
    <div class="dish">
      <div class="dish-head"><span class="dish-name">Traditional Lotuvan Soup</span><span class="dish-price">$21.00</span></div>
      <p class="dish-desc">A mild spicy sweet and sour soup with fish &amp; mushrooms.</p>
    </div>
  </div>

  <div class="abs plate" role="img" aria-label="Fish amok in banana leaf" style="left:398px; top:20px; width:72px; height:60px; background:radial-gradient(circle,#e08a2e 0 35%,#f1efec 70%);"></div>
  <div class="abs plate" role="img" aria-label="Red curry bowl" style="left:398px; top:98px; width:72px; height:66px; background:radial-gradient(circle,#b9c45a 0 40%,#f1efec 70%);"></div>
  <div class="abs plate" role="img" aria-label="Green curry plate" style="left:398px; top:184px; width:74px; height:60px; background:radial-gradient(circle,#c65a2a 0 38%,#f1efec 70%);"></div>
  <div class="abs plate" role="img" aria-label="Kampot pepper seafood" style="left:398px; top:264px; width:74px; height:62px; background:radial-gradient(circle,#b5452a 0 38%,#f1efec 70%);"></div>
  <div class="abs plate" role="img" aria-label="Beef loc lac with fried egg" style="left:400px; top:346px; width:72px; height:72px; background:radial-gradient(circle,#6b3a24 0 38%,#f1efec 70%);"></div>
  <div class="abs plate" role="img" aria-label="Sweet and sour soup bowl" style="left:404px; top:438px; width:64px; height:64px; background:radial-gradient(circle,#d9c9b4 0 40%,#f4f4f2 70%);"></div>

  <div class="abs" role="img" aria-label="Dark bowl of sweet sticky rice with corn and coconut on a banana leaf" style="left:0; top:560px; width:470px; height:290px; border-radius:0 70% 0 0; background:radial-gradient(ellipse at 40% 70%,#e8c64a 0%,#5a3b2a 40%,#2d2a26 70%,#2f5a2a 100%);"></div>

  <div class="abs dish" style="left:530px; top:30px; width:340px;">
    <div class="dish-head" style="grid-template-columns:1fr 50px;"><span class="dish-name">Pumpkin Custard</span><span class="dish-price">$9.00</span></div>
    <p class="dish-desc">Soft pumpkin custard filled sweet coconut cream .</p>
  </div>
  <div class="abs plate" role="img" aria-label="Pumpkin custard" style="left:800px; top:10px; width:58px; height:52px; background:radial-gradient(circle,#c9a25a 0 40%,#f1efec 70%);"></div>

  <h2 class="abs section-head" style="left:530px; top:110px;">Salads</h2>
  <div class="abs side-list" style="left:530px; top:176px; width:320px;">
    <div class="dish"><div class="dish-head"><span class="dish-name">Glass Noodle Salad</span><span class="dish-price">$20.00</span></div><p class="dish-desc">With Chicken or Pork.</p></div>
    <div class="dish"><div class="dish-head"><span class="dish-name">Beef Salad</span><span class="dish-price">$22.00</span></div><p class="dish-desc">With home made dressing &amp; herbs.</p></div>
    <div class="dish"><div class="dish-head"><span class="dish-name">Tofu Salad</span><span class="dish-price">$19.50</span></div><p class="dish-desc">Mixed Asian salad with herbs &amp; coconut dressing .</p></div>
  </div>

  <h2 class="abs section-head" style="left:530px; top:392px;">SIDE DISH</h2>
  <div class="abs side-list" style="left:530px; top:462px; width:320px;">
    <div class="dish-head"><span class="dish-name">Steamed Jasmine Rice</span><span class="dish-price">$3.00</span></div>
    <div class="dish-head"><span class="dish-name">Steamed Vegetable</span><span class="dish-price">$5.00</span></div>
    <div class="dish-head"><span class="dish-name">Steamed Noodle</span><span class="dish-price">$4.00</span></div>
    <div class="dish-head"><span class="dish-name">Rice Peanut</span><span class="dish-price">$5.50</span></div>
    <div class="dish-head"><span class="dish-name">Peanut Sauce</span><span class="dish-price">$4.00</span></div>
  </div>

  <div class="abs" role="img" aria-label="Fresh herbs, chillies, garlic and shallots with a stone mortar" style="left:1040px; top:0; width:160px; height:290px; border-radius:0 0 0 40%; background:linear-gradient(160deg,#2f6b2a,#3f8a34 40%,#b8874a 70%,#c04a5a);"></div>

  <div class="abs title-rule" style="left:878px; top:312px; width:46px;"></div>
  <div class="abs menu-title" style="left:926px; top:296px; width:120px; font-size:16px; letter-spacing:10px; padding-left:10px;">MENU</div>
  <div class="abs title-rule" style="left:1048px; top:312px; width:46px;"></div>

  <div class="abs brand-name" style="left:880px; top:350px; width:260px; font-size:54px;">Lotuvan</div>

  <ul class="abs notes" style="left:900px; top:470px; width:250px;">
    <li>10% surcharge on public holiday</li>
    <li>All price are included GST</li>
    <li>All price are subject to be change without prior notice</li>
    <li>If you are concerned with allergies to certain ingredients please inform our staff</li>
    <li>Food ingredients and price are subject to be changed with prior notice</li>
  </ul>

  <div class="abs legend" style="left:530px; top:770px; width:640px; font-size:14px; gap:24px;">
    <span><i class="dot" style="width:13px;height:13px;background:var(--veg)"></i>Vegetarian</span>
    <span><i class="dot" style="width:13px;height:13px;background:var(--vegan)"></i>Vegan</span>
    <span><i class="dot" style="width:13px;height:13px;background:var(--gf)"></i>Gluten free</span>
    <span><svg width="8" height="12" viewBox="0 0 6 8"><path d="M4 0 Q1 3 2 8 Q5 4 4 0Z" fill="var(--chili)"/></svg>Rate of Spicy</span>
    <span><i class="dot" style="width:11px;height:11px;border-radius:2px;background:#e3a458"></i>Contain Peanut</span>
  </div>
</section>

<!-- Front side: tasty bites, Khmer breakfast, grill, welcome -->
<section class="sheet sheet-front">
  <div class="abs brand-name" style="left:24px; top:84px; width:220px; font-size:46px;">Lotuvan</div>

  <div class="abs title-rule" style="left:344px; top:68px; width:97px;"></div>
  <h1 class="abs menu-title" style="left:510px; top:46px; width:220px; font-size:34px;">MENU</h1>
  <div class="abs title-rule" style="left:745px; top:68px; width:97px;"></div>

  <h2 class="abs section-head" style="left:57px; top:201px;">Tasty Bites</h2>
  <div class="abs dish-list" style="left:57px; top:268px; width:300px; gap:8px;">
    <div class="dish"><div class="dish-head"><span class="dish-name">Betel Leaf</span><span class="dish-price">$4.5</span></div>
      <p class="dish-desc">A traditional Cambodian appetizer, betel leafs with Asian Pomegranate, prawns, herbs and special Lotuvan sauce with a dust of peanuts or coconut shredded (1 pcs).</p></div>
    <div class="dish"><div class="dish-head"><span class="dish-name">Crispy Sweet Potatoes</span><span class="dish-price">$6.0</span></div>
      <p class="dish-desc">Fritted finger strips of sweet potatoes served in a bowl.</p></div>
    <div class="dish"><div class="dish-head"><span class="dish-name">Spring Rolls</span><span class="dish-price">$10.20</span></div>
      <p class="dish-desc">Deep fired roll with pork and prawns, vegetable (3 pcs).</p></div>
    <div class="dish"><div class="dish-head"><span class="dish-name">Vegetarian Spring Rolls</span><span class="dish-price">$10.00</span></div>
      <p class="dish-desc">Sea scallop with herbs and special Lotuvan dressing (2 pcs).</p></div>
  </div>

  <div class="abs plate" role="img" aria-label="Betel leaf appetizer" style="left:368px; top:258px; width:66px; height:66px; background:radial-gradient(circle,#6f8b3c 0 25%,#f1efec 60%);"></div>
  <div class="abs plate" role="img" aria-label="Crispy sweet potato strips" style="left:372px; top:344px; width:58px; height:56px; background:radial-gradient(circle,#e0702b 0 35%,#f1efec 70%);"></div>
  <div class="abs plate" role="img" aria-label="Spring rolls" style="left:372px; top:410px; width:58px; height:54px; background:radial-gradient(circle,#d9a446 0 40%,#f1efec 72%);"></div>
  <div class="abs plate" role="img" aria-label="Vegetarian spring rolls with dipping sauce" style="left:370px; top:474px; width:62px; height:58px; background:radial-gradient(circle,#8a6b4a 0 25%,#eef0ea 65%);"></div>

  <div class="abs" role="img" aria-label="Grilled chicken with rice, lettuce and fresh salad in a white bowl" style="left:0; top:554px; width:441px; height:296px; border-radius:0 60% 0 0; background:radial-gradient(ellipse at 45% 70%,#c46a2c 0%,#b48a58 35%,#d9d9d6 65%,#4f7a2d 90%);"></div>

  <div class="abs" style="left:482px; top:116px; width:330px;">
    <h2 class="section-head boxed">Khmer Breakfast or Lunch</h2>
    <div class="dish-list" style="margin-top:22px;">
      <div class="dish"><div class="dish-head"><span class="dish-name">Kuy Teav Phnom Penh</span><span class="dish-price">$15.50<small>Seafood (+$2.00)</small></span></div>
        <p class="dish-desc">Traditional Cambodian noodle soup, rice and yellow noodles, choice of Pork, Beef or Seafood.</p></div>
      <div class="dish"><div class="dish-head"><span class="dish-name">Lot Cha</span><span class="dish-price">$14.50</span></div>
        <p class="dish-desc">Rice drop noodles with Chinese chives, bean sprouts, chicken, beef ham and a dust of special Lotuvan sauce.</p></div>
      <div class="dish"><div class="dish-head"><span class="dish-name">Kuy Teav Char</span><span class="dish-price">$14.80</span></div>
        <p class="dish-desc">Stir-fired rice noodles, minced pork, ham, egg, bean sprouts and peanut sauce.</p></div>
      <div class="dish"><div class="dish-head"><span class="dish-name">Lemongrass Fried Rice</span><span class="dish-price">$16.50</span></div>
        <p class="dish-desc">Lemongrass, onion, chicken or beef carrot and French beans.</p></div>
    </div>
    <h2 class="section-head boxed" style="margin-top:18px;">Grill</h2>
    <div class="dish-list" style="margin-top:22px;">
      <div class="dish"><div class="dish-head"><span class="dish-name">Beef Skewers with Papaya Salad</span><span class="dish-price">$14.50</span></div>
        <p class="dish-desc">Beef Skewers (4 pcs) with Papaya Salad served with a slice of baguette.</p></div>
      <div class="dish"><div class="dish-head"><span class="dish-name">My Grandmothers Dish</span><span class="dish-price">$17.00</span></div>
        <p class="dish-desc">Grilled chicken tights with brown rice and tomato salad.</p></div>
      <div class="dish"><div class="dish-head"><span class="dish-name">Grilled Corn Cob</span><span class="dish-price">$8.00</span></div>
        <p class="dish-desc">Grilled corn with coconut glaze and spring onion (2 per serve).</p></div>
      <div class="dish"><div class="dish-head"><span class="dish-name">Old School Spareribs</span><span class="dish-price">$25.00</span></div>
        <p class="dish-desc">Grilled pork rib with mixed spices and served with carrot salad.</p></div>
      <div class="dish"><div class="dish-head"><span class="dish-name">Grilled Pork Neck</span><span class="dish-price">$26.00</span></div>
        <p class="dish-desc">Grilled Pork Neck with tamarin sauce, mixed salad and jasmine rice.</p></div>
    </div>
  </div>

  <div class="abs plate" role="img" aria-label="Noodle soup bowl" style="left:826px; top:180px; width:64px; height:60px; background:radial-gradient(circle,#d8c89a 0 35%,#f1efec 70%);"></div>
  <div class="abs plate" role="img" aria-label="Stir-fried rice drop noodles" style="left:826px; top:250px; width:64px; height:64px; background:radial-gradient(circle,#5b3a22 0 45%,#f1efec 72%);"></div>
  <div class="abs plate" role="img" aria-label="Stir-fried rice noodles with egg" style="left:826px; top:326px; width:64px; height:64px; background:radial-gradient(circle,#e7e1cf 0 45%,#f4f4f2 72%);"></div>
  <div class="abs plate" role="img" aria-label="Lemongrass fried rice" style="left:826px; top:396px; width:64px; height:64px; background:radial-gradient(circle,#e2b366 0 50%,#f1efec 75%);"></div>
  <div class="abs" role="img" aria-label="Beef and vegetable skewers" style="left:820px; top:534px; width:80px; height:44px; border-radius:18px; background:linear-gradient(160deg,#c0392b,#6b3b1f 50%,#e0a23a);"></div>
  <div class="abs plate" role="img" aria-label="Grilled chicken with rice" style="left:822px; top:598px; width:76px; height:52px; background:radial-gradient(ellipse,#8a7355 0 35%,#eef0f2 70%);"></div>
  <div class="abs" role="img" aria-label="Grilled corn cobs" style="left:826px; top:670px; width:76px; height:32px; border-radius:16px; background:linear-gradient(90deg,#e8b02c,#f2c649 60%,#6b9a3a);"></div>
  <div class="abs" role="img" aria-label="Grilled spareribs" style="left:824px; top:720px; width:78px; height:42px; border-radius:14px; background:linear-gradient(160deg,#6b3a1c,#a0592a 50%,#4a2a14);"></div>
  <div class="abs plate" role="img" aria-label="Grilled pork neck with salad" style="left:834px; top:782px; width:52px; height:52px; background:radial-gradient(circle,#7a4a35 0 35%,#f1efec 70%);"></div>

  <div class="abs" role="img" aria-label="Blue plate of coconut rice cakes on a tropical leaf" style="left:910px; top:0; width:290px; height:380px; border-radius:0 0 0 55%; background:radial-gradient(circle at 50% 40%,#2d6fb3 0 30%,#1f8a4a 44%,#2f9e52 70%,transparent 72%);"></div>

  <div class="abs about" style="left:918px; top:398px;">
    <p>The founder, who has a Cambodian and French background, loves to cook for people and has put a lot of patience and love to give people an understand of traditional royal food of Cambodia (Le Royal Du Cambodge).</p>
    <p>The food is made from humble beginnings and has developed into great tasting plates through our staff loving what they do, doing great work and enjoying seeing satisfied customers.</p>
    <p>Lotuvan Cafe &amp; Restaurant is committed to excellence and providing friendly welcoming service from chef to our head of Human Resources.</p>
    <p>We embrace an environment of teamwork and personal growth.</p>
    <p>Welcome to Lotuvan Cafe &amp; Restaurant</p>
  </div>

  <div class="abs brand-name" style="left:930px; top:730px; width:200px; font-size:34px;">Lotuvan</div>

  <div class="abs legend" style="left:930px; top:800px; width:220px; font-size:7.5px; gap:4px 10px;">
    <span><i class="dot" style="width:7px;height:7px;background:var(--veg)"></i>Vegetarian</span>
    <span><i class="dot" style="width:7px;height:7px;background:var(--vegan)"></i>Vegan</span>
    <span><i class="dot" style="width:7px;height:7px;background:var(--gf)"></i>Gluten free</span>
    <span><svg width="6" height="8" viewBox="0 0 6 8"><path d="M4 0 Q1 3 2 8 Q5 4 4 0Z" fill="var(--chili)"/></svg>Rate of Spicy</span>
    <span><i class="dot" style="width:7px;height:7px;border-radius:2px;background:#e3a458"></i>Contain Peanut</span>
  </div>
</section>

</body>
</html>
```